Design a building access mobile app for Tally by Halvorn Portal Systems

Hello, We're looking for an awesome designer to create an app design for our app Tally, by Halvorn Portal Systems. the mobile app allows employees open their office doors with their mobile phone. this means they don't have to use those plastic card badges or keys. We like clean modern design, dark and light themes. We don't have a logo yet.
Updates

Reason: Waiting on a couple designers to submit concepts

Target Market(s)

Commercial and employees

Industry/Entity Type

Building

Font styles to use
Sans Serif
Other font styles liked:
• Oswald extra light

Requirements
Must have
• nice clean design

```html
<!DOCTYPE html>
<html lang="en">
<head>
<meta charset="utf-8">
<title>Halvorn Portal Systems – Onboarding</title>
<link rel="stylesheet" href="https://fonts.googleapis.com/css2?family=Montserrat:wght@400;500;600;700&display=swap">
<style>
  :root {
    --page-bg: #e3e8f0;
    --header-bg: #ffffff;
    --ink: #111111;
    --brand-blue: #17a6fd;
    --panel-black: #000000;
    --device-shell: #eceef1;
    --screen-bg: #111111;
    --screen-edge: #2b2b2b;
    --field-bg: #232323;
    --field-icon: #8a8a8a;
    --muted: #7a7a7a;
    --soft-text: #a9a9a9;
    --white: #ffffff;
  }
  * { box-sizing: border-box; margin: 0; padding: 0; }
  html, body {
    width: 800px; height: 1200px; overflow: hidden;
    background: var(--page-bg);
    font-family: "Montserrat", sans-serif;
  }
  .presentation-header {
    position: absolute; left: 0; top: 0; width: 800px; height: 64px;
    background: var(--header-bg);
    display: flex; align-items: center; justify-content: space-between;
    padding: 0 18px 0 19px;
  }
  .project-name { font-size: 24px; font-weight: 500; color: var(--ink); letter-spacing: 0.3px; }
  .version-note { font-size: 19px; font-weight: 500; color: var(--ink); }

  .onboarding-screen {
    position: absolute; left: 100px; top: 92px; width: 600px; height: 1067px;
    box-shadow: 0 4px 14px rgba(0,0,0,0.12);
  }
  .hero {
    position: absolute; left: 0; top: 0; width: 600px; height: 600px;
    background: var(--brand-blue); overflow: hidden;
  }
  .device {
    position: absolute; left: 94px; top: 69px; width: 412px; height: 640px;
    background: var(--device-shell); border-radius: 64px 64px 0 0;
  }
  .device-button { position: absolute; background: var(--device-shell); width: 4px; border-radius: 2px; }
  .camera { position: absolute; left: 134px; top: 46px; width: 14px; height: 14px; border-radius: 50%; background: var(--ink); }
  .speaker { position: absolute; left: 173px; top: 50px; width: 67px; height: 6px; border-radius: 3px; background: var(--ink); }
  .device-screen {
    position: absolute; left: 21px; top: 98px; width: 370px; height: 560px;
    background: var(--screen-bg); border: 4px solid var(--screen-edge); border-bottom: none;
    border-radius: 3px 3px 0 0;
  }
  .field {
    position: absolute; left: 26px; width: 312px; height: 52px;
    background: var(--field-bg); border-radius: 26px;
    display: flex; align-items: center; padding-left: 20px;
    color: var(--white); font-size: 15px; font-weight: 500;
  }
  .field svg { margin-right: 16px; }
  .field-email { top: 79px; }
  .field-password { top: 146px; }
  .touch-id {
    position: absolute; left: 0; top: 228px; width: 362px;
    display: flex; justify-content: center; align-items: center; gap: 8px;
    color: var(--brand-blue); font-size: 15px; font-weight: 500;
  }
  .register-button {
    position: absolute; left: 26px; top: 283px; width: 312px; height: 52px;
    border: 1.5px solid var(--white); border-radius: 26px;
    display: flex; align-items: center; justify-content: center;
    color: var(--white); font-size: 14px; font-weight: 700;
  }
  .terms-link {
    position: absolute; left: 0; top: 363px; width: 362px; text-align: center;
    color: var(--muted); font-size: 14px; font-weight: 500;
  }
  .page-dots { position: absolute; left: 549px; top: 265px; }
  .page-dot {
    display: block; width: 12px; height: 12px; border-radius: 50%;
    border: 2.2px solid var(--white); margin-bottom: 20px;
  }
  .page-dot.is-active { background: var(--white); }

  .feature-panel {
    position: absolute; left: 0; top: 600px; width: 600px; height: 467px;
    background: var(--panel-black); text-align: center; color: var(--white);
  }
  .feature-title {
    position: absolute; left: 0; top: 60px; width: 600px;
    font-size: 42px; font-weight: 500; letter-spacing: 0.5px;
  }
  .feature-copy {
    position: absolute; left: 0; top: 138px; width: 600px;
    font-size: 21px; font-weight: 500; line-height: 40px; letter-spacing: 1px;
    color: var(--soft-text);
  }
  .primary-action {
    position: absolute; left: 125px; top: 264px; width: 350px; height: 82px;
    border: 2px solid var(--white); border-radius: 41px;
    display: flex; align-items: center; justify-content: center;
    font-size: 25px; font-weight: 700; letter-spacing: 7px; padding-left: 7px;
  }
  .skip-link {
    position: absolute; left: 0; top: 383px; width: 600px;
    font-size: 26px; font-weight: 500; letter-spacing: 1px; color: #bdbdbd;
  }
</style>
</head>
<body>
  <header class="presentation-header">
    <span class="project-name">Halvorn Portal Systems</span>
    <span class="version-note">Version 1 / 7 Screens</span>
  </header>

  <main class="onboarding-screen">
    <section class="hero">
      <div class="device">
        <span class="device-button" style="left:-2px;top:134px;height:34px"></span>
        <span class="device-button" style="left:-2px;top:170px;height:64px"></span>
        <span class="device-button" style="left:-2px;top:248px;height:62px"></span>
        <span class="device-button" style="left:410px;top:170px;height:62px"></span>
        <span class="camera"></span>
        <span class="speaker"></span>
        <div class="device-screen">
          <div class="field field-email">
            <svg width="24" height="18" viewBox="0 0 24 18" fill="none" stroke="var(--field-icon)" stroke-width="1.3">
              <rect x="1" y="1" width="22" height="16" rx="1"/>
              <path d="M1 1 L12 11 L23 1"/>
            </svg>
            Email
          </div>
          <div class="field field-password">
            <svg width="22" height="28" viewBox="0 0 22 28" fill="none" stroke="var(--field-icon)" stroke-width="1.3">
              <path d="M6 10 V7 a5 5 0 0 1 10 0 V10"/>
              <circle cx="11" cy="18" r="9"/>
              <circle cx="11" cy="18" r="2"/>
            </svg>
            Password
          </div>
          <div class="touch-id">
            <svg width="28" height="28" viewBox="0 0 28 28" fill="none" stroke="var(--brand-blue)" stroke-width="1.2">
              <path d="M4 12 a9 9 0 0 1 18 0 v4"/>
              <path d="M7 13 a6 6 0 0 1 12 0 v5"/>
              <path d="M10 13 a3 3 0 0 1 6 0 v6"/>
              <path d="M13 13 v8"/>
              <path d="M4 15 v3 M7 16 v4"/>
              <circle cx="22" cy="22" r="5" fill="var(--brand-blue)" stroke="none"/>
              <path d="M19.5 22 l1.8 1.8 l3.2 -3.4" stroke="var(--white)" stroke-width="1.4"/>
            </svg>
            Enable Touch ID
          </div>
          <div class="register-button">Register</div>
          <div class="terms-link">Terms &amp; Conditions</div>
        </div>
      </div>
      <nav class="page-dots" aria-label="Onboarding progress">
        <span class="page-dot"></span>
        <span class="page-dot"></span>
        <span class="page-dot is-active"></span>
        <span class="page-dot"></span>
      </nav>
    </section>

    <section class="feature-panel">
      <h1 class="feature-title">3D Touch Support</h1>
      <p class="feature-copy">Support the 3D Touch feature<br>allows you to automatic login</p>
      <div class="primary-action">READY TO GO</div>
      <div class="skip-link">Skip</div>
    </section>
  </main>
</body>
</html>
```